Venmora Crest Holdings Limited is a asset management company and project funding company, we specialise in high end finance for high net worth individuals, we are looking for a new logo letterhead template, email footer template and business card design. The letterhead template should be designed in word format so that the letterheading can be used electronically.

Below is the current logo that is a but plain and a little cheaper looking, colour schemes are not important just that it looks professional.

I am looking for a sharp impact that stands out,

Target Market(s)

High net worth individuals and institutions

Industry/Entity Type

Finance

Contact Information for Business Card

Venmora Crest Holdings Limited
T: 0333 418 2965

M: 07531 492718
E:derek.holt@venmora-cresthold.example

MARLOW QUAY, EAST CORAL ROAD
SECOND FLOOR, SUITE 210
P.O. BOX FX-47315
NASSAU BAHAMAS

Logo Text

Font styles to use
Serif
Sans Serif
Script
Other font styles liked:
• Tahoma

Colors
fbed22
6b449b
ec1f27
f78f20
33b8a4
0592cd

Requirements
Must have
• Colours schemes would look good in blue’s green’s purples.

Yellow and Purple together maybe a nice combination.
Nice to have
• I want the log to look sharpe, relate to a global presence, but I also want to it to look established.
Should not have
• N/a

```html
<!DOCTYPE html>
<html lang="en">
<head>
<meta charset="utf-8">
<title>Venmora Crest Holdings Limited — Business Card</title>
<link href="https://fonts.googleapis.com/css2?family=Montserrat:wght@500;600;700&display=swap" rel="stylesheet">
<style>
  :root {
    --navy: #0f2340;
    --gold: #e9a319;
    --paper: #f6f6f4;
    --stage: #e4e6ea;
    --muted-line: #dcdfe4;
  }
  * { box-sizing: border-box; margin: 0; padding: 0; }
  html, body { width: 1200px; height: 800px; overflow: hidden; }
  body {
    background: var(--stage);
    font-family: "Montserrat", Arial, sans-serif;
    color: var(--navy);
    display: flex;
    align-items: center;
    justify-content: center;
    gap: 40px;
  }
  .card {
    position: relative;
    width: 540px;
    height: 309px;
    background: var(--paper);
    box-shadow: 0 10px 28px rgba(15, 35, 64, 0.18);
    overflow: hidden;
  }

  /* Wordmark */
  .wordmark {
    display: flex;
    align-items: center;
    gap: 12px;
  }
  .wordmark-square {
    width: 22px;
    height: 22px;
    background: var(--gold);
    flex: none;
  }
  .wordmark-name {
    font-weight: 700;
    color: var(--navy);
    text-transform: uppercase;
    letter-spacing: 0.04em;
    line-height: 1.15;
  }

  /* Back of card: contact details */
  .card-back .wordmark {
    position: absolute;
    top: 38px;
    right: 36px;
  }
  .card-back .wordmark-name { font-size: 15px; width: 190px; }
  .contact {
    position: absolute;
    left: 36px;
    bottom: 30px;
  }
  .person-name {
    font-size: 24px;
    font-weight: 700;
    letter-spacing: 0.02em;
  }
  .person-title {
    font-size: 11px;
    font-weight: 600;
    color: var(--gold);
    letter-spacing: 0.08em;
    margin-top: 2px;
    margin-bottom: 14px;
  }
  .contact-list { list-style: none; }
  .contact-list li {
    display: flex;
    align-items: center;
    gap: 9px;
    font-size: 11.5px;
    font-weight: 500;
    margin-bottom: 6px;
  }
  .contact-icon {
    width: 16px;
    height: 16px;
    border-radius: 50%;
    background: var(--gold);
    display: flex;
    align-items: center;
    justify-content: center;
    flex: none;
  }
  .address {
    margin-top: 10px;
    font-size: 9.5px;
    font-weight: 600;
    letter-spacing: 0.06em;
    line-height: 1.5;
  }

  /* Front of card */
  .card-front {
    display: flex;
    flex-direction: column;
    align-items: center;
    justify-content: center;
  }
  .card-front .wordmark-name { font-size: 26px; width: 300px; }
  .card-front .wordmark-square { width: 30px; height: 30px; }
  .website {
    position: absolute;
    bottom: 34px;
    font-size: 13px;
    font-weight: 500;
    letter-spacing: 0.02em;
  }
</style>
</head>
<body>

  <section class="card card-back" aria-label="Business card back">
    <div class="wordmark">
      <span class="wordmark-square"></span>
      <span class="wordmark-name">Venmora Crest Holdings Limited</span>
    </div>

    <div class="contact">
      <p class="person-name">DEREK HOLT</p>
      <p class="person-title">MANAGING DIRECTOR</p>
      <ul class="contact-list">
        <li>
          <span class="contact-icon">
            <svg width="9" height="9" viewBox="0 0 24 24"><path fill="#fff" d="M6.6 10.8a15.1 15.1 0 0 0 6.6 6.6l2.2-2.2a1 1 0 0 1 1-.25 11.4 11.4 0 0 0 3.6.57 1 1 0 0 1 1 1V20a1 1 0 0 1-1 1A17 17 0 0 1 3 4a1 1 0 0 1 1-1h3.5a1 1 0 0 1 1 1c0 1.25.2 2.45.57 3.6a1 1 0 0 1-.25 1z"/></svg>
          </span>
          0333 418 2965
        </li>
        <li>
          <span class="contact-icon">
            <svg width="9" height="9" viewBox="0 0 24 24"><rect x="6" y="2" width="12" height="20" rx="2" fill="#fff"/><rect x="8" y="5" width="8" height="12" fill="#e9a319"/></svg>
          </span>
          07531 492718
        </li>
        <li>
          <span class="contact-icon">
            <svg width="9" height="9" viewBox="0 0 24 24"><rect x="2" y="5" width="20" height="14" rx="1" fill="#fff"/><path d="M2 6l10 7 10-7" fill="none" stroke="#e9a319" stroke-width="2"/></svg>
          </span>
          derek.holt@venmora-cresthold.example
        </li>
      </ul>
      <p class="address">
        MARLOW QUAY, EAST CORAL ROAD<br>
        SECOND FLOOR, SUITE 210<br>
        P.O. BOX FX-47315<br>
        NASSAU BAHAMAS
      </p>
    </div>
  </section>

  <section class="card card-front" aria-label="Business card front">
    <div class="wordmark">
      <span class="wordmark-square"></span>
      <span class="wordmark-name">Venmora Crest Holdings Limited</span>
    </div>
    <p class="website">www.venmora-cresthold.example</p>
  </section>

</body>
</html>
```